Tallow & Mersey Needs New Stationery / Letterhead Design

We need new stationery to match our new logo (attached). Tallow & Mersey is a 34 year old nationwide law firm located in Houston Tx. They do personal injury law and pharmaceutical litigation.

WE DO NOT NEED BUSINESS CARDS.

Attached are several different file formats of the new logo.

Reason: We will make a decision in the next couple days. Finalizing edits now. Thank you!

Target Market(s)

consumers who have been injured due to the negligence of another or by a pharmaceutical drug or defective medical device. Also co-counsel and opposing counsel (law firms0.

Industry/Entity Type

Law Firm

Requirements
Must have
• logo
• Tallow & Mersey, LLP
• 7183 Corvid Lane, Suite 1000
• Brenford, TX 75591
• Tel: (555) 408-1936
• Fax: (555) 408-2275
• www.tallowandmersey.example
• Must have colors in the logo.
• Make the font go with the logo - not necessarily the same, but something that goes well with it.

```html
<!DOCTYPE html>
<html lang="en">
<head>
<meta charset="utf-8">
<title>Tallow &amp; Mersey — Letterhead</title>
<link rel="stylesheet" href="https://fonts.googleapis.com/css2?family=Cinzel:wght@400;600&family=Crimson+Text&family=Open+Sans:wght@400;600;700&family=Great+Vibes&display=swap">
<style>
  :root {
    --navy: #1f3a68;
    --ink: #1b1b1b;
    --paper: #f5f5f4;
    --backdrop: #6c6d72;
  }
  * { box-sizing: border-box; margin: 0; padding: 0; }
  html, body { width: 1200px; height: 1040px; overflow: hidden; }
  body { background: var(--backdrop); position: relative; font-family: "Open Sans", sans-serif; color: var(--ink); }

  .letterhead {
    position: absolute; left: 240px; top: 10px;
    width: 720px; height: 1020px;
    background: var(--paper);
    box-shadow: 0 6px 24px rgba(0,0,0,.35);
  }

  .brand { position: absolute; left: 70px; top: 92px; display: flex; align-items: center; gap: 10px; }
  .brand-square { width: 22px; height: 22px; background: var(--navy); }
  .brand-name { font-family: "Cinzel", serif; font-weight: 600; font-size: 23px; color: var(--navy); letter-spacing: .5px; }

  .practice-band {
    position: absolute; left: 322px; top: 32px; right: 0; height: 20px;
    background: var(--navy); color: #fff;
    font-family: "Crimson Text", serif; font-size: 12px; letter-spacing: .8px;
    line-height: 20px; padding-left: 10px; text-transform: uppercase;
  }
  .practice-band svg { position: absolute; left: -8px; top: -6px; }

  .practice-list { position: absolute; top: 64px; list-style: none; font-family: "Crimson Text", serif; font-size: 12.5px; color: #2a2a2a; }
  .practice-list li { height: 14.7px; line-height: 14.7px; display: flex; align-items: center; gap: 7px; }
  .practice-list.col-a { left: 330px; }
  .practice-list.col-b { left: 525px; }
  .tick { width: 9px; height: 9px; flex: none; }

  .subject { position: absolute; left: 72px; top: 276px; font-size: 12px; font-weight: 700; }
  .dateline { position: absolute; right: 70px; top: 298px; font-size: 12px; }
  .salutation { position: absolute; left: 72px; top: 325px; font-size: 13px; }

  .body-copy { position: absolute; left: 72px; width: 580px; font-size: 12.1px; line-height: 15.6px; }
  .body-copy span { display: block; text-align: justify; text-align-last: justify; white-space: nowrap; }
  .body-copy span.end { text-align-last: left; }

  .closing { position: absolute; left: 76px; top: 763px; font-size: 11.5px; }
  .signature { position: absolute; left: 64px; top: 782px; font-family: "Great Vibes", cursive; font-size: 40px; color: var(--ink); }

  .footer { position: absolute; left: 0; right: 0; top: 882px; text-align: center; color: var(--navy); }
  .footer-title { font-family: "Cinzel", serif; font-size: 23px; color: #2a2a2a; letter-spacing: 1px; }
  .footer-firm { display: flex; align-items: center; justify-content: center; gap: 8px; margin-top: 2px; }
  .footer-firm .rule { width: 160px; height: 1.5px; background: var(--navy); }
  .footer-firm .name { font-family: "Cinzel", serif; font-size: 16px; letter-spacing: .6px; }
  .footer-contact { font-size: 11.5px; line-height: 15.5px; margin-top: 2px; }
  .footer-contact b { font-weight: 700; }
</style>
</head>
<body>
<main class="letterhead">
  <div class="brand">
    <div class="brand-square"></div>
    <div class="brand-name">Tallow &amp; Mersey</div>
  </div>

  <div class="practice-band">
    <svg width="14" height="14" viewBox="0 0 14 14"><path d="M0 6 L12 0 L12 6 Z" fill="var(--navy)"/></svg>
    Prescription Drug and Medical Device Failures
  </div>

  <ul class="practice-list col-a">
    <li><svg class="tick" viewBox="0 0 10 10"><rect x=".5" y=".5" width="9" height="9" fill="none" stroke="var(--navy)"/><path d="M2 5 L4.2 7.3 L8.3 2.3" fill="none" stroke="var(--navy)" stroke-width="1.4"/></svg>Automobile Accidents</li>
    <li><svg class="tick" viewBox="0 0 10 10"><rect x=".5" y=".5" width="9" height="9" fill="none" stroke="var(--navy)"/><path d="M2 5 L4.2 7.3 L8.3 2.3" fill="none" stroke="var(--navy)" stroke-width="1.4"/></svg>Trucking Accidents</li>
    <li><svg class="tick" viewBox="0 0 10 10"><rect x=".5" y=".5" width="9" height="9" fill="none" stroke="var(--navy)"/><path d="M2 5 L4.2 7.3 L8.3 2.3" fill="none" stroke="var(--navy)" stroke-width="1.4"/></svg>Motorcycle Accidents</li>
    <li><svg class="tick" viewBox="0 0 10 10"><rect x=".5" y=".5" width="9" height="9" fill="none" stroke="var(--navy)"/><path d="M2 5 L4.2 7.3 L8.3 2.3" fill="none" stroke="var(--navy)" stroke-width="1.4"/></svg>Boating &amp; Watercraft Accidents</li>
    <li><svg class="tick" viewBox="0 0 10 10"><rect x=".5" y=".5" width="9" height="9" fill="none" stroke="var(--navy)"/><path d="M2 5 L4.2 7.3 L8.3 2.3" fill="none" stroke="var(--navy)" stroke-width="1.4"/></svg>Qui Tam Litigation</li>
    <li><svg class="tick" viewBox="0 0 10 10"><rect x=".5" y=".5" width="9" height="9" fill="none" stroke="var(--navy)"/><path d="M2 5 L4.2 7.3 L8.3 2.3" fill="none" stroke="var(--navy)" stroke-width="1.4"/></svg>Construction Accidents</li>
  </ul>
  <ul class="practice-list col-b">
    <li><svg class="tick" viewBox="0 0 10 10"><rect x=".5" y=".5" width="9" height="9" fill="none" stroke="var(--navy)"/><path d="M2 5 L4.2 7.3 L8.3 2.3" fill="none" stroke="var(--navy)" stroke-width="1.4"/></svg>Medical Malpractice</li>
    <li><svg class="tick" viewBox="0 0 10 10"><rect x=".5" y=".5" width="9" height="9" fill="none" stroke="var(--navy)"/><path d="M2 5 L4.2 7.3 L8.3 2.3" fill="none" stroke="var(--navy)" stroke-width="1.4"/></svg>Wrongful Death</li>
    <li><svg class="tick" viewBox="0 0 10 10"><rect x=".5" y=".5" width="9" height="9" fill="none" stroke="var(--navy)"/><path d="M2 5 L4.2 7.3 L8.3 2.3" fill="none" stroke="var(--navy)" stroke-width="1.4"/></svg>Defective Design</li>
    <li><svg class="tick" viewBox="0 0 10 10"><rect x=".5" y=".5" width="9" height="9" fill="none" stroke="var(--navy)"/><path d="M2 5 L4.2 7.3 L8.3 2.3" fill="none" stroke="var(--navy)" stroke-width="1.4"/></svg>Unsafe Products</li>
    <li><svg class="tick" viewBox="0 0 10 10"><rect x=".5" y=".5" width="9" height="9" fill="none" stroke="var(--navy)"/><path d="M2 5 L4.2 7.3 L8.3 2.3" fill="none" stroke="var(--navy)" stroke-width="1.4"/></svg>Property Liability</li>
    <li><svg class="tick" viewBox="0 0 10 10"><rect x=".5" y=".5" width="9" height="9" fill="none" stroke="var(--navy)"/><path d="M2 5 L4.2 7.3 L8.3 2.3" fill="none" stroke="var(--navy)" stroke-width="1.4"/></svg>Business Disputes</li>
  </ul>

  <p class="subject">Oggetto: Lorem Ipsum is simply dummy text.</p>
  <p class="dateline">Saudi Arabia, 01/05/2017</p>
  <p class="salutation">Dear Dana,</p>

  <p class="body-copy" style="top:355px">
    <span>Lorem Ipsum is simply dummy text of the printing and typesetting industry. Lorem Ipsum has been the</span>
    <span>industry's standard dummy text ever since the 1500s, when an unknown printer took a galley of type</span>
    <span>and scrambled it to make a type specimen book. It has survived not only five centuries, but also the leap</span>
    <span>into electronic typesetting, remaining essentially unchanged. It was popularised in the 1960s with the</span>
    <span class="end">release of Pressfold sheets containing Lorem Ipsum passages, and more recently with desktop publish</span>
  </p>
  <p class="body-copy" style="top:449px">
    <span>Lorem Ipsum is simply dummy text of the printing and typesetting industry. Lorem Ipsum has been the</span>
    <span>industry's standard dummy text ever since the 1500s, when an unknown printer took a galley of type</span>
    <span>and scrambled it to make a type specimen book. It has survived not only five centuries, but also the leap</span>
    <span>into electronic typesetting, remaining essentially unchanged. It was popularised in the 1960s with the</span>
  </p>
  <p class="body-copy" style="top:531px">
    <span>Lorem Ipsum is simply dummy text of the printing and typesetting industry. Lorem Ipsum has been the</span>
    <span>industry's standard dummy text ever since the 1500s, when an unknown printer took a galley of type</span>
    <span>and scrambled it to make a type specimen book. It has survived not only five centuries, but also the leap</span>
    <span>into electronic typesetting, remaining essentially unchanged. It was popularised in the 1960s with the</span>
    <span class="end">release of Pressfold sheets containing Lorem Ipsum passages, and more recently with desktop publish</span>
  </p>
  <p class="body-copy" style="top:625px">
    <span>Lorem Ipsum is simply dummy text of the printing and typesetting industry. Lorem Ipsum has been the</span>
    <span>industry's standard dummy text ever since the 1500s, when an unknown printer took a galley of type</span>
    <span>and scrambled it to make a type specimen book. It has survived not only five centuries, but also the leap</span>
    <span>into electronic typesetting, remaining essentially unchanged. It was popularised in the 1960s with the</span>
  </p>
  <p class="body-copy" style="top:706px">
    <span>Lorem Ipsum is simply dummy text of the printing and typesetting industry. Lorem Ipsum has been the</span>
    <span class="end">industry's standard dummy text ever since the 1500.</span>
  </p>

  <p class="closing">Cordiali Saluti</p>
  <p class="signature">Signature</p>

  <footer class="footer">
    <div class="footer-title">A PERSONAL INJURY LAW FIRM</div>
    <div class="footer-firm"><span class="rule"></span><span class="name">Tallow &amp; Mersey, LLP</span><span class="rule"></span></div>
    <div class="footer-contact">
      7183 Corvid Lane, Suite 1000 &nbsp;•&nbsp; Brenford, Texas 75591<br>
      <b>Tel</b> (555) 408-1936 &nbsp;•&nbsp; <b>Toll Free</b> (555) LAW-0190 &nbsp;•&nbsp; <b>Fax</b> (555) 408-2275<br>
      intake@tallowandmersey.example &nbsp;•&nbsp; www.tallowandmersey.example
    </div>
  </footer>
</main>
</body>
</html>
```